Northstar Leadership Transformation Roadmap

I've included a mock up of what I like. This design needs to be made better. I like the top section layout. It needs 5 circles for:

Please create a webpage based on this design, but improve it. Use the letterhead and business card brand you created for me to make the brand look seamless.

I love the circles - please make 5 of them the same size (can be 1 lines)

Here is the text for the circles:

Headline: Your Guided Path to Transformation
Text
Step 1: The Initial Consultation
text
Step 2: Deep-Dive Discovery and Assessment
text
Step 3: Synthesis and Strategy Formulation
text
Step 4: The Strategic Debrief Session
Text
Step 5: Implementation and Ongoing Support
Text

Also, there are many sections to this page including:

Introduction
Copy
Copy
Bio
CTA
FAQ's

Please make it interesting.

Use the colors of the mockup and my website: Corinne Valdez.com
I am including my letterhead and business card for brand coherence.

Use the fonts on my website. CorinneValdez.com

I will need all files to send to the developer. We must have ALL the art files.

Target Market(s)

see my website; CorinneValdez.com

Industry/Entity Type

See my uploads

Requirements
Must have
• all the design files

```html
<!DOCTYPE html>
<html lang="en">
<head>
<meta charset="utf-8">
<title>Northstar Leadership Transformation Roadmap</title>
<link href="https://fonts.googleapis.com/css2?family=Playfair+Display:wght@400;500&family=Poppins:wght@300;400;500&display=swap" rel="stylesheet">
<style>
:root{
  --navy:#141a45;
  --navy-deep:#0f1438;
  --gold:#c8a96e;
  --gold-light:#e3cc9a;
  --teal:#3a87a6;
  --ink:#1f2340;
  --text:#3b3f55;
  --white:#ffffff;
  --line:#d9c49a;
  --soft:#d8daea;
}
*{box-sizing:border-box;margin:0;padding:0}
html,body{width:1200px;height:5231px;overflow:hidden;background:var(--white)}
body{font-family:'Poppins',sans-serif;color:var(--text);position:relative}
.page{position:relative;width:1200px;height:5231px;overflow:hidden}
.abs{position:absolute}
.serif{font-family:'Playfair Display',serif;font-weight:400}
.btn{position:absolute;display:flex;align-items:center;justify-content:center;background:var(--gold);color:var(--white);font-size:11px;font-family:'Poppins',sans-serif;letter-spacing:.2px}
p{font-size:11px;line-height:1.6}

/* brand name */
.brand{position:absolute;font-family:'Poppins',sans-serif;font-weight:400;font-size:16px;color:var(--white);text-align:center;white-space:nowrap}

/* hero */
.hero{position:absolute;left:0;top:0;width:1200px;height:890px;background:radial-gradient(ellipse 420px 220px at 620px 60px,#3a3d63 0%,rgba(20,26,69,0) 70%),var(--navy)}
.nav{position:absolute;top:40px;right:95px;display:flex;gap:30px;font-size:11px;color:var(--white)}
.hero-photo{position:absolute;left:130px;top:140px;width:430px;height:700px;border-radius:215px 215px 0 0;background:radial-gradient(ellipse at 50% 30%,#b58a6a 0%,#6b4a3c 30%,#1e2752 65%,var(--navy) 100%)}
.hero-title{position:absolute;left:580px;top:200px;width:510px;text-align:center;color:var(--gold);font-size:40px;line-height:1.15}
.hero-copy{position:absolute;left:585px;top:302px;width:525px;text-align:center;color:var(--soft);font-size:10.5px;line-height:1.55}

/* steps */
.section-title{position:absolute;left:0;width:1200px;text-align:center;color:var(--ink);font-size:38px;line-height:1.2}
.step-label{position:absolute;width:180px;text-align:center;font-family:'Playfair Display',serif;font-size:13.5px;line-height:1.25;color:var(--ink)}

/* bio */
.bio-name{position:absolute;left:90px;top:1468px;font-size:38px;color:var(--ink)}
.bio-copy{position:absolute;left:90px;top:1530px;width:465px}
.bio-copy p{color:var(--text);margin-bottom:10px;font-size:10.5px}

/* stats */
.stats{position:absolute;left:0;top:1948px;width:1200px;height:250px;background:var(--navy)}
.stat{position:absolute;top:100px}
.stat .num{font-family:'Playfair Display',serif;font-size:36px;color:var(--gold);line-height:1}
.stat .lbl{font-size:11px;color:var(--soft);margin-top:8px}

/* benefits */
.benefit{position:absolute;width:405px}
.benefit h3{font-family:'Playfair Display',serif;font-weight:400;font-size:17px;color:var(--gold);margin-bottom:14px}
.benefit p{font-size:10.5px;color:var(--text)}

/* retreat */
.retreat-img{position:absolute;left:0;top:3068px;width:597px;height:428px;background:linear-gradient(160deg,#6f7d3a 0%,#9a8a4c 30%,#5d6b2c 55%,#8b6a3e 80%,#4e5a26 100%)}

/* blog */
.blog{position:absolute;left:0;top:3496px;width:1200px;height:548px;background:linear-gradient(180deg,var(--navy) 0%,#1f2350 45%,#3a2f55 75%,var(--navy) 100%)}
.blog-img{position:absolute;left:595px;top:170px;width:480px;height:284px;background:radial-gradient(circle at 55% 45%,#ffe9a6 0%,#f2a94e 14%,#c4603f 35%,#5a3d63 65%,#2b2d59 100%)}
.meta{position:absolute;left:155px;top:290px;display:flex;gap:22px;font-size:10px;color:var(--gold);align-items:center}
.meta span{display:flex;align-items:center;gap:6px}

/* faq */
.faq-item{position:absolute;left:232px;width:736px;height:50px;border:1.5px solid var(--line);display:flex;align-items:center;justify-content:space-between;padding:0 24px 0 30px;font-size:12px;color:var(--ink);background:var(--white)}
.faq-item .plus{color:var(--gold);font-size:18px;font-weight:300}

/* footer */
.footer{position:absolute;left:0;top:4600px;width:1200px;height:631px}
.foot-col h4{font-family:'Playfair Display',serif;font-weight:400;font-size:17px;color:var(--gold);margin-bottom:12px}
.foot-col a{display:block;font-size:10.5px;color:var(--soft);text-decoration:none;margin-bottom:9px}
</style>
</head>
<body>
<div class="page">

  <!-- HERO -->
  <section class="hero">
    <div class="hero-photo" role="img" aria-label="Portrait of Corinne Valdez in a navy blazer, arms crossed"></div>
    <div class="brand" style="left:92px;top:110px;width:180px">Northstar Leadership</div>
    <nav class="nav">
      <span>Coaching</span><span>Retreats</span><span>About &#8964;</span><span>Insights</span><span>Contact</span>
    </nav>
    <h1 class="hero-title serif">Northstar Leadership<br>Transformation Roadmap</h1>
    <p class="hero-copy">Elite Coaching with Corinne Valdez — Your organization—and its challenges—are unlike any other. Generic training can only take your leaders so far. To achieve the profound, lasting impact your vision demands, you need a solution crafted specifically for you.</p>
    <div class="btn" style="left:762px;top:370px;width:174px;height:42px">Book a Discovery Call</div>
    <svg class="abs" style="left:0;top:480px" width="1200" height="410" viewBox="0 0 1200 410">
      <path d="M0,360 C260,330 470,210 700,150 C900,100 1080,60 1200,40 L1200,410 L0,410 Z" fill="#ffffff"/>
      <path d="M560,240 C760,150 980,80 1200,64 L1200,90 C990,106 780,175 600,250 Z" fill="#3a87a6"/>
      <path d="M0,380 C200,390 420,300 620,200 C450,300 240,370 0,372 Z" fill="#c8a96e"/>
      <path d="M0,398 C250,400 440,320 640,215" fill="none" stroke="#3a87a6" stroke-width="3"/>
    </svg>
  </section>

  <!-- GUIDED PATH -->
  <h2 class="section-title serif" style="top:884px">Your Guided Path to<br>Transformation</h2>
  <svg class="abs" style="left:0;top:1000px" width="1200" height="300" viewBox="0 0 1200 300">
    <path d="M106,150 A99 99 0 0 1 304,150 A99 99 0 0 0 502,150 A99 99 0 0 1 700,150 A99 99 0 0 0 898,150 A99 99 0 0 1 1096,150" fill="none" stroke="#141a45" stroke-width="3"/>
    <circle cx="106" cy="150" r="6" fill="#3a87a6"/>
    <circle cx="1096" cy="150" r="6" fill="#3a87a6"/>
    <g fill="#c8a96e">
      <circle cx="205" cy="150" r="66"/><circle cx="403" cy="150" r="66"/><circle cx="601" cy="150" r="66"/><circle cx="799" cy="150" r="66"/><circle cx="997" cy="150" r="66"/>
    </g>
    <g fill="none" stroke="#c8a96e" stroke-width="1.5">
      <circle cx="205" cy="150" r="73"/><circle cx="403" cy="150" r="73"/><circle cx="601" cy="150" r="73"/><circle cx="799" cy="150" r="73"/><circle cx="997" cy="150" r="73"/>
    </g>
    <g fill="none" stroke="#ffffff" stroke-width="2" stroke-linecap="round" stroke-linejoin="round">
      <circle cx="205" cy="132" r="9"/><path d="M187,172 C187,155 223,155 223,172"/>
      <rect x="383" y="128" width="34" height="28" rx="2"/><path d="M389,137 H411 M389,144 H404"/><circle cx="418" cy="160" r="7"/><path d="M423,165 L429,171"/>
      <circle cx="601" cy="150" r="10"/><circle cx="601" cy="150" r="20" stroke-dasharray="6 5"/>
      <circle cx="786" cy="140" r="6"/><circle cx="799" cy="136" r="7"/><circle cx="812" cy="140" r="6"/><path d="M778,166 C778,152 820,152 820,166"/>
      <path d="M981,154 A16 16 0 0 1 1013,154"/><rect x="977" y="152" width="7" height="12" rx="2"/><rect x="1010" y="152" width="7" height="12" rx="2"/><path d="M1013,164 C1013,172 1004,174 999,174"/>
    </g>
    <g font-family="Playfair Display, serif" font-size="13" fill="#ffffff" text-anchor="middle">
      <circle cx="205" cy="51" r="13" fill="#3a87a6"/><text x="205" y="56">1</text>
      <circle cx="403" cy="249" r="13" fill="#3a87a6"/><text x="403" y="254">2</text>
      <circle cx="601" cy="51" r="13" fill="#3a87a6"/><text x="601" y="56">3</text>
      <circle cx="799" cy="249" r="13" fill="#3a87a6"/><text x="799" y="254">4</text>
      <circle cx="997" cy="51" r="13" fill="#3a87a6"/><text x="997" y="56">5</text>
    </g>
  </svg>
  <div class="step-label" style="left:115px;top:1246px">The Initial<br>Consultation</div>
  <div class="step-label" style="left:313px;top:1020px">Deep-Dive Discovery<br>and Assessment</div>
  <div class="step-label" style="left:511px;top:1246px">Synthesis and Strategy<br>Formulation</div>
  <div class="step-label" style="left:709px;top:1020px">The Strategic<br>Debrief Session</div>
  <div class="step-label" style="left:907px;top:1246px">Implementation and<br>Ongoing Support</div>

  <!-- BIO -->
  <h2 class="bio-name serif">Corinne Valdez</h2>
  <div class="bio-copy">
    <p>As a top leader, you deserve an elite partnership designed exclusively for you—especially when you need a woman you can count on. With a perspective rooted in both wisdom and empathy, I offer insights, intuition, and support that many male coaches simply cannot replicate.</p>
    <p>My mission is to guide high-performing leaders and their teams toward a state of peak performance defined by stress-free resilience, heightened productivity, and effortless flow. I founded Corinne Valdez International to provide effective, accelerated training that unlocks the highest levels of human potential. I am especially passionate about empowering executives and senior-level management to lead with clarity, impact, and well-being.</p>
  </div>
  <div class="btn" style="left:91px;top:1733px;width:176px;height:42px">Book a Discovery Call</div>
  <svg class="abs" style="left:585px;top:1370px" width="520" height="520" viewBox="0 0 520 520">
    <defs>
      <linearGradient id="ring" x1="0" y1="0" x2="1" y2="1">
        <stop offset="0" stop-color="#8a6a33"/><stop offset=".35" stop-color="#e9d29a"/><stop offset=".7" stop-color="#c8a96e"/><stop offset="1" stop-color="#ffffff" stop-opacity="0"/>
      </linearGradient>
      <radialGradient id="portrait" cx="50%" cy="40%" r="60%">
        <stop offset="0" stop-color="#b58a6a"/><stop offset=".35" stop-color="#7a5440"/><stop offset=".7" stop-color="#d6bb86"/><stop offset="1" stop-color="#c8a96e"/>
      </radialGradient>
    </defs>
    <circle cx="268" cy="265" r="250" fill="none" stroke="url(#ring)" stroke-width="12"/>
    <circle cx="270" cy="275" r="230" fill="url(#portrait)" role="img" aria-label="Portrait of Corinne Valdez on a gold background"/>
  </svg>

  <!-- STATS -->
  <section class="stats">
    <div class="stat" style="left:100px"><div class="num">25 Years</div><div class="lbl">Experience</div></div>
    <div class="stat" style="left:350px"><div class="num">15,00+</div><div class="lbl">Transformational Sessions</div></div>
    <div class="stat" style="left:622px"><div class="num">#1 National</div><div class="lbl">Bestselling Author</div></div>
    <div class="stat" style="left:928px"><div class="num">700+</div><div class="lbl">Licensable Training Materials</div></div>
  </section>

  <!-- BENEFITS -->
  <h2 class="section-title serif" style="top:2296px">Core Benefits of<br>Elite Coaching for Leaders</h2>
  <p class="abs" style="left:240px;top:2403px;width:720px;text-align:center;font-size:10.5px">Elite coaching provides a confidential, strategic partnership designed to elevate the performance of top executives and their organizations. This bespoke service focuses on the specific, high-stakes challenges that leaders face. Below is an expansion of the core benefits you can expect from this exclusive engagement.</p>
  <svg class="abs" style="left:0;top:2478px" width="1200" height="520" viewBox="0 0 1200 520">
    <line x1="600" y1="0" x2="600" y2="226" stroke="#c8a96e" stroke-width="1.5"/>
    <line x1="600" y1="294" x2="600" y2="520" stroke="#c8a96e" stroke-width="1.5"/>
    <line x1="95" y1="260" x2="566" y2="260" stroke="#c8a96e" stroke-width="1.5"/>
    <line x1="634" y1="260" x2="1105" y2="260" stroke="#c8a96e" stroke-width="1.5"/>
    <circle cx="600" cy="260" r="34" fill="#ffffff" stroke="#c8a96e" stroke-width="1.5"/>
    <circle cx="600" cy="260" r="18" fill="none" stroke="#3a87a6" stroke-width="2"/>
  </svg>
  <div class="benefit" style="left:140px;top:2535px">
    <h3>Exclusivity and Tailored Strategies</h3>
    <p>This is not a one-size-fits-all program. Your coaching experience is designed exclusively for you, your leadership style, and your organization's unique circumstances. We develop a completely customized roadmap that addresses your specific goals and challenges. This bespoke approach ensures our work is highly relevant and impactful, moving beyond generic leadership theories to create practical, actionable strategies that drive tangible results in your specific context.</p>
  </div>
  <div class="benefit" style="left:651px;top:2535px">
    <h3>Strategic Decision-Making</h3>
    <p>As a leader, you face complex decisions with far-reaching consequences. Elite coaching provides a confidential sounding board to pressure-test ideas, explore potential outcomes, and gain clarity on the best path forward. We work together to sharpen your analytical skills, enhance your foresight, and build a repeatable framework for making sound, strategic choices under pressure, ensuring you lead with confidence and conviction.</p>
  </div>
  <div class="benefit" style="left:142px;top:2805px">
    <h3>Leadership Development</h3>
    <p>Even the most accomplished leaders have room to grow. This coaching focuses on refining your unique leadership capabilities, whether that means enhancing your executive presence, inspiring high-performing teams, or leading transformative change. We identify and amplify your strengths while addressing any blind spots that may be limiting your impact, ensuring your leadership continues to evolve and meet the demands of your role.</p>
  </div>
  <div class="benefit" style="left:651px;top:2805px">
    <h3>Navigating Organizational Challenges</h3>
    <p>From internal politics and cultural shifts to external market disruptions, leaders must steer their organizations through constant change. Elite coaching provides expert guidance and an objective perspective to help you navigate these complexities. We partner to develop strategies for managing conflict, aligning stakeholders, and leading your organization through periods of uncertainty or transformation with stability and clear direction.</p>
  </div>

  <!-- RETREAT -->
  <div class="retreat-img" role="img" aria-label="Aerial view of a wooden lodge with a terraced deck and umbrellas surrounded by lush forest"></div>
  <h2 class="abs serif" style="left:663px;top:3150px;font-size:36px;line-height:1.22;color:var(--ink)">The 2026 Northstar Leadership<br>Transformation Retreat</h2>
  <p class="abs" style="left:663px;top:3243px;font-size:10.5px;color:var(--ink)">Revitalize – Renew – Reimagine</p>
  <p class="abs" style="left:663px;top:3270px;width:440px;font-size:10.5px;color:var(--text)">An exclusive transformational retreat package for executives, entrepreneurs and small business owners</p>
  <div class="btn" style="left:663px;top:3328px;width:176px;height:42px">Book a Discovery Call</div>

  <!-- BLOG -->
  <section class="blog">
    <h2 class="abs serif" style="left:0;top:92px;width:1200px;text-align:center;font-size:36px;color:var(--gold)">Insights &amp; Blog</h2>
    <h3 class="abs serif" style="left:155px;top:205px;font-size:29px;line-height:1.25;color:var(--white)">Transform Your Leadership<br>Style with Corinne Valdez</h3>
    <div class="meta">
      <span><svg width="11" height="11" viewBox="0 0 12 12" fill="none" stroke="#c8a96e" stroke-width="1.2"><circle cx="6" cy="4" r="2.5"/><path d="M1.5,11 C1.5,7 10.5,7 10.5,11"/></svg>Corinne Valdez</span>
      <span><svg width="11" height="11" viewBox="0 0 12 12" fill="none" stroke="#c8a96e" stroke-width="1.2"><rect x="1" y="2" width="10" height="9"/><path d="M1,5 H11 M4,1 V3 M8,1 V3"/></svg>April 2, 2024</span>
      <span><svg width="11" height="11" viewBox="0 0 12 12" fill="none" stroke="#c8a96e" stroke-width="1.2"><circle cx="6" cy="6" r="5"/><path d="M6,3 V6 L8,7.5"/></svg>10:35 pm</span>
    </div>
    <p class="abs" style="left:155px;top:318px;width:380px;font-size:10.5px;color:var(--soft)">Leadership in today's changing business environment goes beyond task management and operations. Inspire, motivate, and lead a team to an...</p>
    <div class="btn" style="left:155px;top:378px;width:106px;height:42px">Read More</div>
    <div class="blog-img" role="img" aria-label="Sunrise over layered mountain ridges"></div>
  </section>

  <!-- FAQ -->
  <h2 class="section-title serif" style="top:4140px">Northstar Leadership Coaching<br>Suggested FAQ Section</h2>
  <div class="faq-item" style="top:4272px"><span>What is Northstar Leadership Coaching?</span><span class="plus">+</span></div>
  <div class="faq-item" style="top:4328px"><span>Who is this coaching designed for?</span><span class="plus">+</span></div>
  <div class="faq-item" style="top:4384px"><span>How is Northstar Leadership Coaching different from other leadership programs?</span><span class="plus">+</span></div>
  <div class="faq-item" style="top:4440px"><span>What types of organizations has Corinne worked with?</span><span class="plus">+</span></div>
  <div class="faq-item" style="top:4496px"><span>What results can I expect from Elite Coaching?</span><span class="plus">+</span></div>
  <div class="btn" style="left:530px;top:4566px;width:140px;height:44px">View More FAQS</div>

  <!-- FOOTER -->
  <footer class="footer">
    <svg class="abs" style="left:0;top:0" width="1200" height="631" viewBox="0 0 1200 631">
      <path d="M0,40 C200,20 420,80 640,170 C860,250 1050,250 1200,230 L1200,631 L0,631 Z" fill="#141a45"/>
      <path d="M0,30 C200,10 420,70 640,160 C860,240 1050,240 1200,220 L1200,240 C1050,258 860,258 640,178 C420,92 200,40 0,60 Z" fill="#c8a96e"/>
      <path d="M600,170 C800,250 1000,265 1200,250 L1200,280 C1000,292 800,272 600,180 Z" fill="#3a87a6"/>
    </svg>
    <div class="brand" style="left:245px;top:410px;width:200px">Northstar Leadership</div>
    <p class="abs" style="left:160px;top:458px;width:370px;text-align:center;font-size:10.5px;line-height:1.5;color:var(--soft)">Northstar Leadership Transformation is a trade name owned by Corinne Valdez International and The Resonant Wellness Institute.</p>
    <div class="abs foot-col" style="left:625px;top:405px">
      <h4>Useful Links</h4>
      <a>2026 Retreat</a><a>About</a><a>Insights</a>
    </div>
    <div class="abs foot-col" style="left:858px;top:405px">
      <h4>Support</h4>
      <a>Terms &amp; Policies</a><a>Membership Agreement</a><a>Contact</a>
    </div>
    <p class="abs" style="left:0;top:598px;width:1200px;text-align:center;font-size:10.5px;color:var(--soft)">Copyright © 2025. All rights reserved.</p>
  </footer>

</div>
</body>
</html>
```